The Brightfield Lease Group Flyer to entice people to call us.

We negotiate contracts for phone masts (commercial leases). We also sell phone masts, remove phone masts, oversee the build of phone masts etc but act only for landlords. Our website is www.brightfieldleasegroup.co.uk and i would like the flyer to reflect the branding and colour scheme on it. Ideally, i would like a tri-fold flyer. One page should be our contact details. You can use the images i have uploaded but also, you can use some of your own if you feel there are appropriate (ie people etc). We want to project the image of looking after landlords who have phone masts and making them a lot of money. I can provide the section titles and wording.

Target Market(s)

Landowners, can be big corporations like Varnells or Utility companies- or farmers and people who own buildings.

Industry/Entity Type

Telecommunications

Font styles to use
Sans Serif

Requirements
Must have
• Must have our colour scheme from our website (www.brightfieldleasegroup.co.uk), must look modern and catchy, must have our contact details, must have pictures of one stand alone mast (tower) and one rooftop mast. Must have our logo (which should be attached).
Nice to have
• Perhaps some pictures of people looking happy, maybe an old couple, maybe a picture of a corporate individual, punchy headings.

```html
<!DOCTYPE html>
<html lang="en">
<head>
<meta charset="utf-8">
<title>The Brightfield Lease Group – Tri-fold Flyer</title>
<link rel="stylesheet" href="https://fonts.googleapis.com/css2?family=Open+Sans:wght@400;600;700&display=swap">
<style>
  :root {
    --green: #3e6e26;
    --green-dark: #2c5419;
    --green-light: #6a9a3c;
    --ink: #4a4a4a;
    --paper: #ffffff;
    --paper-shade: #e4e4e4;
    --frame: #c9c9c9;
    --backdrop: #efefed;
    --sky: #6f9fd8;
    --sky-pale: #b9d2ee;
    --field: #7e8f4a;
  }
  * { box-sizing: border-box; margin: 0; padding: 0; }
  html, body { width: 1200px; height: 900px; overflow: hidden; }
  body {
    background: var(--backdrop);
    font-family: "Open Sans", Arial, sans-serif;
    color: var(--ink);
  }
  .flyer {
    position: absolute; left: 30px; top: 47px;
    width: 1140px; height: 806px;
    display: flex;
    box-shadow: 0 4px 18px rgba(0,0,0,.12);
  }
  .panel {
    position: relative; width: 380px; height: 100%;
    background: var(--paper); overflow: hidden;
  }
  .panel + .panel { border-left: 1px solid #e6e6e6; }
  .panel--middle { background: linear-gradient(to bottom, var(--paper) 60%, var(--paper-shade)); }

  .heading {
    color: var(--green); font-weight: 400; text-transform: uppercase;
    letter-spacing: .01em; line-height: 1.1;
  }
  .body-copy { font-size: 11.4px; line-height: 1.45; }

  .photo {
    position: absolute; border: 6px solid var(--frame);
  }
  .photo--field { background: linear-gradient(to bottom, var(--sky) 0%, var(--sky-pale) 55%, var(--field) 75%, #5f7233 100%); }
  .photo--tower { border: none; background: linear-gradient(to bottom, #4f86cf 0%, #8fb6e4 55%, #a9c6e6 72%, #56733c 85%, #3f5a2c 100%); }
  .photo--rooftop { background: linear-gradient(to bottom, #7faee0, #c9dcef); }

  .banner {
    position: absolute; background: var(--green); color: #fff;
  }

  /* left */
  .sell-heading { position: absolute; left: 24px; top: 28px; font-size: 17px; }
  .sell-photo { left: 0; top: 60px; width: 300px; height: 206px; border-left: none; }
  .sell-copy { position: absolute; left: 24px; top: 280px; width: 334px; }
  .getting-heading { position: absolute; left: 24px; top: 452px; font-size: 22px; }
  .getting-copy { position: absolute; left: 24px; top: 490px; width: 334px; }
  .rooftop-photo { left: 14px; top: 676px; width: 116px; height: 94px; }
  .make-most {
    left: 140px; top: 650px; width: 240px; height: 112px;
    padding: 28px 0 0 30px; font-size: 17px; line-height: 1.25;
  }
  .make-most::before {
    content: ""; position: absolute; left: -14px; top: 44px;
    border-style: solid; border-width: 12px 14px 12px 0;
    border-color: transparent var(--green) transparent transparent;
  }

  /* middle */
  .tower-photo { left: 0; top: 0; width: 380px; height: 340px; }
  .rent-banner {
    left: 0; top: 282px; width: 380px; height: 64px;
    padding: 13px 18px 0 22px; font-size: 11.2px; line-height: 1.5;
  }
  .climate-heading { position: absolute; left: 22px; top: 384px; font-size: 16px; }
  .climate-copy { position: absolute; left: 22px; top: 412px; width: 340px; }

  /* right */
  .intro-copy { position: absolute; left: 20px; top: 24px; width: 342px; }
  .advice-banner {
    left: 0; top: 300px; width: 380px; height: 70px;
    padding: 11px 20px 0 20px; font-size: 11.5px; line-height: 1.45;
  }
  .advice-banner strong { font-weight: 700; display: block; }
  .advice-banner .web { display: flex; align-items: center; gap: 6px; margin-top: 3px; }
  .services-heading { position: absolute; left: 20px; top: 400px; font-size: 17px; }
  .services-list {
    position: absolute; left: 20px; top: 430px; list-style: none;
    font-size: 13px; line-height: 1.62; color: #222;
  }
  .services-list li { display: flex; align-items: center; gap: 8px; }
  .call-bar {
    left: 0; top: 720px; width: 380px; height: 46px;
    display: flex; align-items: center; justify-content: space-between;
    padding: 0 20px; font-size: 14px;
  }
  .call-bar .phone { display: flex; align-items: center; gap: 7px; font-weight: 700; font-size: 17px; }
</style>
</head>
<body>
<main class="flyer">

  <section class="panel panel--left">
    <h2 class="heading sell-heading">Sell Your Phone Mast</h2>
    <div class="photo photo--field sell-photo" role="img" aria-label="Photo of a standalone phone mast in a grassy field under blue sky"></div>
    <p class="body-copy sell-copy">We can also assist landlords in selling their phone mast. We have strong links with many large investors who regularly purchase the freehold or leasehold interest of masts and will pay a cash lump sum, often even hundreds of thousands of pounds. This can be done in a matter of weeks and the cash is yours to spend however you like, regardless of whether the mast stays for the duration of the investor's leasehold or not. We can negotiate flexible terms, such as a buyback option so please call us today to discuss.</p>
    <h2 class="heading getting-heading">Getting a Phone Mast</h2>
    <p class="body-copy getting-copy">If you don't currently have a mast located on your land but are interested in receiving thousands of pounds a year in rental income, or you have a redundant mast you would like to market, we offer a free advertising service on our website. We will market your land to phone mast operators with a view to having a mast located there. Please visit the 'Advertise My Site' link on our website to take advantage of this service.</p>
    <div class="photo photo--rooftop rooftop-photo" role="img" aria-label="Photo of a rooftop phone mast against the sky"></div>
    <div class="banner make-most">Make the most<br>from your phone mast</div>
  </section>

  <section class="panel panel--middle">
    <div class="photo photo--tower tower-photo" role="img" aria-label="Photo of a tall lattice phone mast tower beside trees and an equipment cabin"></div>
    <div class="banner rent-banner">If you would like to know what rent your mast should be achieving,<br>check out the free rent estimation service on our website</div>
    <h2 class="heading climate-heading">The Current Telecoms Climate</h2>
    <p class="body-copy climate-copy">The telecoms market, in relation to mobile phone masts, is going through some huge changes. Operators are combining to cut costs. We have already seen Northlink join forces with Corvel Mobile, and Tellwave and Arcline form a jointly owned company to share their sites. More recently, Northlink and Corvel Mobile have merged to form Unison Mobile, challenged by the new network leader. Everything is set to become confused again with Halden Holdings buying Arcline and Meridian Telecom hoping to buy Unison Mobile. Well, that's not the end of it! What this can mean for the landlord is changes to their site and potentially the loss of income. It can all be very confusing but don't worry, this is where we can help.</p>
  </section>

  <section class="panel panel--right">
    <p class="body-copy intro-copy">We know the telecoms industry well and understand how a new network deal can affect a landlord. Operators are under pressure to provide the best coverage while cutting costs, and many leases are being reviewed, renegotiated or ended early. Due to all the mergers, there have been and will be more sites which become redundant. Operators will look to reduce rents, share equipment and remove masts that are no longer needed, often giving short notice. Before you respond to any letter, speak to us first. We can review your lease, explain your options and protect your income. Our professional team has years of experience acting only for landlords and will make sure you receive a fair rent for your site.</p>
    <div class="banner advice-banner">
      <strong>Landlords should not sign anything until they have sought professional advice</strong>
      <span class="web">
        <svg width="12" height="12" viewBox="0 0 12 12" aria-hidden="true"><g fill="none" stroke="#fff" stroke-width="1"><circle cx="6" cy="6" r="5"/><ellipse cx="6" cy="6" rx="2.2" ry="5"/><line x1="1" y1="6" x2="11" y2="6"/></g></svg>
        www.brightfieldleasegroup.co.uk
      </span>
    </div>
    <h2 class="heading services-heading">Our Services</h2>
    <ul class="services-list">
      <li><svg width="11" height="11" viewBox="0 0 11 11" aria-hidden="true"><circle cx="5.5" cy="5.5" r="5.5" fill="#6a9a3c"/><path d="M4.3 3l2.5 2.5-2.5 2.5" fill="none" stroke="#fff" stroke-width="1.3"/></svg>Rent Reviews</li>
      <li><svg width="11" height="11" viewBox="0 0 11 11" aria-hidden="true"><circle cx="5.5" cy="5.5" r="5.5" fill="#6a9a3c"/><path d="M4.3 3l2.5 2.5-2.5 2.5" fill="none" stroke="#fff" stroke-width="1.3"/></svg>Lease Renewals</li>
      <li><svg width="11" height="11" viewBox="0 0 11 11" aria-hidden="true"><circle cx="5.5" cy="5.5" r="5.5" fill="#6a9a3c"/><path d="M4.3 3l2.5 2.5-2.5 2.5" fill="none" stroke="#fff" stroke-width="1.3"/></svg>Network Consolidation Issues</li>
      <li><svg width="11" height="11" viewBox="0 0 11 11" aria-hidden="true"><circle cx="5.5" cy="5.5" r="5.5" fill="#6a9a3c"/><path d="M4.3 3l2.5 2.5-2.5 2.5" fill="none" stroke="#fff" stroke-width="1.3"/></svg>Site Shares</li>
      <li><svg width="11" height="11" viewBox="0 0 11 11" aria-hidden="true"><circle cx="5.5" cy="5.5" r="5.5" fill="#6a9a3c"/><path d="M4.3 3l2.5 2.5-2.5 2.5" fill="none" stroke="#fff" stroke-width="1.3"/></svg>Rent Protection</li>
      <li><svg width="11" height="11" viewBox="0 0 11 11" aria-hidden="true"><circle cx="5.5" cy="5.5" r="5.5" fill="#6a9a3c"/><path d="M4.3 3l2.5 2.5-2.5 2.5" fill="none" stroke="#fff" stroke-width="1.3"/></svg>Equipment Upgrades</li>
      <li><svg width="11" height="11" viewBox="0 0 11 11" aria-hidden="true"><circle cx="5.5" cy="5.5" r="5.5" fill="#6a9a3c"/><path d="M4.3 3l2.5 2.5-2.5 2.5" fill="none" stroke="#fff" stroke-width="1.3"/></svg>Mast Removals / Decommissioning</li>
      <li><svg width="11" height="11" viewBox="0 0 11 11" aria-hidden="true"><circle cx="5.5" cy="5.5" r="5.5" fill="#6a9a3c"/><path d="M4.3 3l2.5 2.5-2.5 2.5" fill="none" stroke="#fff" stroke-width="1.3"/></svg>Mast Sales and Marketing</li>
      <li><svg width="11" height="11" viewBox="0 0 11 11" aria-hidden="true"><circle cx="5.5" cy="5.5" r="5.5" fill="#6a9a3c"/><path d="M4.3 3l2.5 2.5-2.5 2.5" fill="none" stroke="#fff" stroke-width="1.3"/></svg>Land Marketing for Masts</li>
      <li><svg width="11" height="11" viewBox="0 0 11 11" aria-hidden="true"><circle cx="5.5" cy="5.5" r="5.5" fill="#6a9a3c"/><path d="M4.3 3l2.5 2.5-2.5 2.5" fill="none" stroke="#fff" stroke-width="1.3"/></svg>Mast Management and Portfolios</li>
      <li><svg width="11" height="11" viewBox="0 0 11 11" aria-hidden="true"><circle cx="5.5" cy="5.5" r="5.5" fill="#6a9a3c"/><path d="M4.3 3l2.5 2.5-2.5 2.5" fill="none" stroke="#fff" stroke-width="1.3"/></svg>Safety Testing</li>
    </ul>
    <div class="banner call-bar">
      <span>Call us now for a free estimate!</span>
      <span class="phone">
        <svg width="18" height="18" viewBox="0 0 18 18" aria-hidden="true"><circle cx="9" cy="9" r="8" fill="none" stroke="#fff" stroke-width="1.3"/><path d="M6.2 4.6l1.5-.3.9 2.1-1 .8c.5 1.2 1.3 2 2.4 2.5l.8-1 2.1.9-.3 1.5c-.2.5-.7.8-1.3.7-3-.6-5.3-2.9-5.9-5.9-.1-.6.2-1.1.8-1.3z" fill="#fff"/></svg>
        01632 960418
      </span>
    </div>
  </section>

</main>
</body>
</html>
```